Lumokrest Mobile App

I need a professional, sleek design for a new mobile application for Zentab. The application will be the mobile counterpart to the current website (www.lumokrest-app.net - please refer to site for existing web design).
Lumokrest is a photo social network which focuses on content aggregation, search and real-time photo discovery.
I need a clean, modern, minimalistic design for the mobile app which will run on Zentab, including minimalistic page and button designs.
I've attached undesigned screenshots of the current application build to give an idea of the functionality and pages available within the application.
The app will have the following pages/functionality:
- photo feed of other users' images; data presented: photo, photo caption, user name, date
- upload photo
- save photo
- photo search; available search criteria: keywords, dates (from/to), location
Photographers/Photo enthusiasts, bloggers, social networking
Build

```html
<!DOCTYPE html>
<html lang="en">
<head>
<meta charset="utf-8">
<title>Lumokrest Mobile App – Home and Upload</title>
<link rel="stylesheet" href="https://fonts.googleapis.com/css2?family=Ubuntu:ital,wght@0,400;0,500;0,700;1,400&family=Source+Sans+3:wght@400;600&display=swap">
<style>
  :root {
    --page-bg: #ffffff;
    --header-bg: #1a1b1d;
    --feed-bg: #2e2f33;
    --feed-edge: #232427;
    --card-bg: #141516;
    --tab-bg: #141517;
    --green: #7fb530;
    --green-light: #9ccc45;
    --green-dark: #5f8e1c;
    --green-text: #2f4a0c;
    --grey-light: #e4e5e7;
    --grey-dark: #a3a5a8;
    --grey-text: #3c3d40;
    --white: #ffffff;
    --caption-sub: #8a8b8f;
    --badge-red: #d9362b;
  }
  * { box-sizing: border-box; margin: 0; padding: 0; }
  html, body { width: 1200px; height: 900px; overflow: hidden; }
  body { background: var(--page-bg); font-family: "Ubuntu", sans-serif; position: relative; }

  .screen {
    position: absolute; top: 135px; width: 324px; height: 572px;
    background: linear-gradient(90deg, var(--feed-edge) 0, var(--feed-bg) 28px, var(--feed-bg) 296px, var(--feed-edge) 324px);
    overflow: hidden;
  }
  .screen--home { left: 163px; }
  .screen--upload { left: 703px; }

  .top-bar {
    position: absolute; left: 0; top: 0; width: 100%; height: 45px;
    background: var(--header-bg);
    display: flex; align-items: center; justify-content: center;
  }
  .screen--upload .top-bar { height: 38px; }
  .top-bar__title { color: var(--white); font-weight: 700; font-size: 17px; letter-spacing: 0.5px; }

  .nav-button {
    position: absolute; top: 50%; transform: translateY(-50%);
    height: 18px; width: 72px;
    background: linear-gradient(var(--green-light), var(--green-dark));
    color: var(--white); font-size: 9px; font-weight: 400; font-family: "Ubuntu", sans-serif;
    display: flex; align-items: center; justify-content: center; gap: 5px;
  }
  .nav-button--back { left: 10px; clip-path: polygon(8px 0, 100% 0, 100% 100%, 8px 100%, 0 50%); padding-left: 6px; }
  .nav-button--forward { right: 10px; clip-path: polygon(0 0, calc(100% - 8px) 0, 100% 50%, calc(100% - 8px) 100%, 0 100%); padding-right: 6px; }
  .nav-button svg { width: 5px; height: 8px; }

  .photo-card {
    position: absolute; left: 28px; width: 267px;
    background: var(--card-bg); border-radius: 3px; padding: 5px 3px 0;
  }
  .photo-card__image { width: 261px; height: 172px; }
  .photo-card__title { color: var(--white); font-size: 12.5px; font-weight: 400; margin: 8px 0 0 2px; line-height: 1.2; }
  .photo-card__author { color: var(--caption-sub); font-size: 6.5px; font-style: italic; margin: 1px 0 0 3px; }

  .card-1 { top: 40px; height: 218px; }
  .card-2 { top: 265px; height: 217px; }
  .card-3 { top: 492px; height: 60px; }

  .image--twilight { background: linear-gradient(160deg, #8a4a3c, #4a3a30); }
  .image--rain { background: linear-gradient(160deg, #6f9a8a, #b8ab7c); }
  .image--bokeh { background: linear-gradient(90deg, #5a3a6a, #8a4a5a); }

  .tab-bar {
    position: absolute; left: 0; bottom: 0; width: 100%; height: 47px;
    background: var(--tab-bg);
  }
  .tab-bar__item { position: absolute; top: 8px; width: 36px; height: 32px; display: flex; align-items: center; justify-content: center; }
  .tab-bar__item svg { width: 34px; height: 28px; }
  .tab-shuffle { left: 32px; }
  .tab-gallery { left: 102px; }
  .tab-upload { left: 176px; }
  .tab-profile { left: 250px; }
  .tab-bar__item--active-box { background: var(--green); border-radius: 2px; }
  .tab-bar__badge {
    position: absolute; top: 1px; right: 2px; width: 9px; height: 9px; border-radius: 50%;
    background: var(--badge-red); color: var(--white); font-size: 6px; line-height: 7px; text-align: center; border: 1px solid var(--white);
  }

  .upload-frame {
    position: absolute; left: 28px; top: 40px; width: 268px; height: 347px;
    background: #1c1d1f; border-radius: 3px; padding: 3px;
  }
  .upload-frame__image { width: 100%; height: 100%; background: linear-gradient(170deg, #3a3634, #6e5a48); }

  .done-button {
    position: absolute; left: 110px; top: 364px; width: 102px; height: 38px;
    background: linear-gradient(var(--green-light), var(--green-dark));
    border-radius: 3px; box-shadow: 0 3px 8px rgba(0,0,0,0.55);
    display: flex; align-items: center; justify-content: center; gap: 5px;
    color: var(--green-text); font-family: "Source Sans 3", sans-serif; font-size: 16px; font-weight: 400;
  }
  .done-button svg { width: 15px; height: 15px; }

  .action-button {
    position: absolute; left: 28px; width: 268px; height: 28px; border-radius: 2px;
    display: flex; align-items: center; justify-content: center;
    font-family: "Source Sans 3", sans-serif; font-size: 15px; font-weight: 400;
  }
  .action-button--primary { top: 410px; background: linear-gradient(var(--green-light), var(--green-dark)); color: var(--green-text); }
  .action-button--secondary { background: linear-gradient(var(--grey-light), var(--grey-dark)); color: var(--grey-text); }
  .action-save { top: 446px; }
  .action-cancel { top: 481px; }
</style>
</head>
<body>

<section class="screen screen--home" aria-label="Home feed screen">
  <header class="top-bar">
    <span class="nav-button nav-button--back"><svg viewBox="0 0 5 8"><path d="M4 0.5 1 4l3 3.5" fill="none" stroke="#1e3306" stroke-width="1.3"/></svg>Sign Out</span>
    <h1 class="top-bar__title">HOME</h1>
    <span class="nav-button nav-button--forward">Search<svg viewBox="0 0 5 8"><path d="M1 0.5 4 4 1 7.5" fill="none" stroke="#1e3306" stroke-width="1.3"/></svg></span>
  </header>

  <article class="photo-card card-1">
    <div class="photo-card__image image--twilight" role="img" aria-label="Photo of a hilltop fort city at twilight"></div>
    <h2 class="photo-card__title">Fort Grey Twilight</h2>
    <p class="photo-card__author">by User McUser</p>
  </article>

  <article class="photo-card card-2">
    <div class="photo-card__image image--rain" role="img" aria-label="Photo of a colourful umbrella reflected in a rain puddle"></div>
    <h2 class="photo-card__title">After Rain Happiness</h2>
    <p class="photo-card__author">by User McUser</p>
  </article>

  <article class="photo-card card-3">
    <div class="photo-card__image image--bokeh" role="img" aria-label="Photo of colourful blurred city lights"></div>
  </article>

  <nav class="tab-bar">
    <span class="tab-bar__item tab-shuffle"><svg viewBox="0 0 34 28"><path d="M3 9h7l12 11h6M3 20h7l4-4M18 12l4-3h6" fill="none" stroke="#fff" stroke-width="3"/><path d="M27 5l5 4-5 4zM27 16l5 4-5 4z" fill="#fff"/></svg></span>
    <span class="tab-bar__item tab-gallery"><svg viewBox="0 0 34 28"><path d="M17 2 4 8h26z" fill="var(--green)"/><rect x="4" y="9" width="26" height="2" fill="var(--green)"/><rect x="7" y="12" width="3" height="10" fill="var(--green)"/><rect x="13" y="12" width="3" height="10" fill="var(--green)"/><rect x="19" y="12" width="3" height="10" fill="var(--green)"/><rect x="25" y="12" width="3" height="10" fill="var(--green)"/><rect x="4" y="23" width="26" height="2" fill="var(--green)"/><rect x="2" y="26" width="30" height="2" fill="var(--green)"/></svg></span>
    <span class="tab-bar__item tab-upload"><svg viewBox="0 0 34 28"><path d="M2 7h9l2-4h8l2 4h9v20H2z" fill="#fff"/><circle cx="17" cy="17" r="7" fill="#141517"/><path d="M17 12l-4 4h2.5v5h3v-5H21z" fill="#fff"/></svg></span>
    <span class="tab-bar__item tab-profile"><svg viewBox="0 0 34 28"><rect x="1" y="4" width="32" height="21" rx="2" fill="#fff"/><circle cx="9" cy="11" r="3" fill="#141517"/><path d="M4 21c0-5 10-5 10 0z" fill="#141517"/><rect x="17" y="9" width="12" height="2" fill="#141517"/><rect x="17" y="13" width="12" height="2" fill="#141517"/><rect x="17" y="17" width="12" height="2" fill="#141517"/></svg></span>
  </nav>
</section>

<section class="screen screen--upload" aria-label="Upload photo screen">
  <header class="top-bar">
    <span class="nav-button nav-button--back"><svg viewBox="0 0 5 8"><path d="M4 0.5 1 4l3 3.5" fill="none" stroke="#1e3306" stroke-width="1.3"/></svg>Sign Out</span>
    <h1 class="top-bar__title">UPLOAD</h1>
    <span class="nav-button nav-button--forward">Search<svg viewBox="0 0 5 8"><path d="M1 0.5 4 4 1 7.5" fill="none" stroke="#1e3306" stroke-width="1.3"/></svg></span>
  </header>

  <div class="upload-frame">
    <div class="upload-frame__image" role="img" aria-label="Photo of a latte with foam art in a cup on a dark table"></div>
  </div>

  <span class="done-button"><svg viewBox="0 0 15 15"><circle cx="7.5" cy="7.5" r="7" fill="var(--green-text)"/><path d="M4 7.5l2.5 2.5 4.5-5" fill="none" stroke="var(--green-light)" stroke-width="2"/></svg>DONE</span>

  <span class="action-button action-button--primary">Upload</span>
  <span class="action-button action-button--secondary action-save">Save to Phone</span>
  <span class="action-button action-button--secondary action-cancel">Cancel</span>

  <nav class="tab-bar">
    <span class="tab-bar__item tab-shuffle"><svg viewBox="0 0 34 28"><path d="M3 9h7l12 11h6M3 20h7l4-4M18 12l4-3h6" fill="none" stroke="#fff" stroke-width="3"/><path d="M27 5l5 4-5 4zM27 16l5 4-5 4z" fill="#fff"/></svg></span>
    <span class="tab-bar__item tab-gallery"><svg viewBox="0 0 34 28"><path d="M17 2 4 8h26z" fill="#fff"/><rect x="4" y="9" width="26" height="2" fill="#fff"/><rect x="7" y="12" width="3" height="10" fill="#fff"/><rect x="13" y="12" width="3" height="10" fill="#fff"/><rect x="19" y="12" width="3" height="10" fill="#fff"/><rect x="25" y="12" width="3" height="10" fill="#fff"/><rect x="4" y="23" width="26" height="2" fill="#fff"/><rect x="2" y="26" width="30" height="2" fill="#fff"/></svg><span class="tab-bar__badge">5</span></span>
    <span class="tab-bar__item tab-upload tab-bar__item--active-box"><svg viewBox="0 0 34 28"><path d="M5 8h7l2-3h6l2 3h7v17H5z" fill="#141517"/><circle cx="17" cy="16.5" r="6" fill="var(--green)"/><path d="M17 12l-3.5 3.5h2v4.5h3v-4.5h2z" fill="#141517"/></svg></span>
    <span class="tab-bar__item tab-profile"><svg viewBox="0 0 34 28"><rect x="1" y="4" width="32" height="21" rx="2" fill="#fff"/><circle cx="9" cy="11" r="3" fill="#141517"/><path d="M4 21c0-5 10-5 10 0z" fill="#141517"/><rect x="17" y="9" width="12" height="2" fill="#141517"/><rect x="17" y="13" width="12" height="2" fill="#141517"/><rect x="17" y="17" width="12" height="2" fill="#141517"/></svg></span>
  </nav>
</section>

</body>
</html>
```